Design a Banner for Velmorix marketing service

I am running a contest because I do not have a design in mind. I am wanting to see your designs. I will choose the best suited one.

I am looking for a advertising banner for one of my websites that is a service for getting more real velmorix followers and photo likes. A majority of the people who use this service are musicians, business owners, marketers, SEO, or just regular people wanting to increase their followers. So its a mix.

The banner idea that I am looking for MUST include some sort of "increase in followers" or "increase in post likes" indication in it. I want the banner to bring the attention that we increase their followers and bring them real fast results.

Text that can be included in banner .

1. Increase your followers = Higher reputation and trust.
2. Get 100% REAL Velmorix followers starting within 24 hours.

I am wanting the logo to be branded on the banner. Therefor, I have attached it to this project.

```html
<!DOCTYPE html>
<html lang="en">
<head>
<meta charset="utf-8">
<title>Increase Your Followers – Tidevault</title>
<link rel="stylesheet" href="https://fonts.googleapis.com/css2?family=Oswald:wght@500;700&family=Barlow+Condensed:ital,wght@1,400;1,600&display=swap">
<style>
  :root {
    --paper-light: #f4e8cf;
    --paper-mid: #e3cca6;
    --paper-edge: #bf9a6e;
    --ink-dark: #3a2418;
    --ink-muted: #9c8068;
    --bar-red: #d93a33;
    --bar-yellow: #fbbf57;
    --bar-orange: #eea034;
    --bar-green: #7bc97b;
    --bar-blue: #4ea4c9;
    --trail-red: #b02f2a;
    --trail-yellow: #eeb255;
    --trail-orange: #d98f2e;
    --trail-green: #5faa66;
    --trail-blue: #3a8fae;
  }
  * { margin: 0; padding: 0; box-sizing: border-box; }
  html, body { width: 1200px; height: 1200px; overflow: hidden; }
  body { background: var(--paper-edge); }
  .banner {
    position: relative;
    width: 1200px;
    height: 1200px;
    overflow: hidden;
    background: radial-gradient(ellipse 70% 65% at 50% 45%, var(--paper-light) 0%, var(--paper-mid) 60%, var(--paper-edge) 100%);
  }
  .chart {
    position: absolute;
    inset: 0;
    width: 1200px;
    height: 1200px;
  }
  .headline {
    position: absolute;
    top: 40px;
    left: 0;
    width: 1200px;
    text-align: center;
    font-family: "Oswald", sans-serif;
    font-weight: 500;
    font-size: 86px;
    line-height: 1;
    letter-spacing: 1px;
    color: var(--ink-dark);
    text-transform: uppercase;
  }
  .tagline {
    position: absolute;
    top: 142px;
    left: 0;
    width: 1200px;
    text-align: center;
    font-family: "Barlow Condensed", sans-serif;
    font-style: italic;
    font-weight: 400;
    font-size: 60px;
    line-height: 1;
    color: var(--ink-muted);
  }
  .tagline strong { font-weight: 600; }
  .brand-name {
    position: absolute;
    top: 1032px;
    left: 0;
    width: 1200px;
    text-align: center;
    font-family: "Oswald", sans-serif;
    font-weight: 700;
    font-size: 76px;
    line-height: 1;
    letter-spacing: 2px;
    color: var(--ink-dark);
    text-transform: uppercase;
  }
</style>
</head>
<body>
  <main class="banner">
    <svg class="chart" viewBox="0 0 500 500" role="img" aria-label="Bar chart showing follower growth">
      <g class="trails">
        <polygon fill="var(--trail-red)" points="120,398 160,398 55,500 0,500 0,470"/>
        <polygon fill="var(--trail-yellow)" points="178,398 218,398 172,500 98,500"/>
        <polygon fill="var(--trail-orange)" points="236,398 276,398 292,500 222,500"/>
        <polygon fill="var(--trail-green)" points="290,398 330,398 425,500 345,500"/>
        <polygon fill="var(--trail-blue)" points="343,398 382,398 500,478 500,500 458,500"/>
      </g>
      <g class="bars">
        <rect fill="var(--bar-red)" x="120" y="178" width="40" height="220"/>
        <rect fill="var(--bar-yellow)" x="178" y="113" width="40" height="285"/>
        <rect fill="var(--bar-orange)" x="236" y="250" width="40" height="148"/>
        <rect fill="var(--bar-green)" x="290" y="160" width="40" height="238"/>
        <rect fill="var(--bar-blue)" x="343" y="211" width="39" height="187"/>
      </g>
    </svg>
    <h1 class="headline">Increase your followers</h1>
    <p class="tagline"><strong>HIGHER</strong> reputation and trust</p>
    <p class="brand-name">Tidevault</p>
  </main>
</body>
</html>
```